Blue Harbor Trophies & Awards Unique Business Card Design

Recently selected a new logo design and waiting to recieve print files. I've attached image for your review. We are a trophies and awards company that provides engraving on trophies, plaques, name plates, name tags, desk sets, medals, acrylics, and signage.

We are located in Monroe, Louisiana and provide this service with computerized & laser engraving equipment.

Target Market(s)

Corporate, Sport, Church, and Special Events

Industry/Entity Type

Business

Contact Information for Business Card

I'd like to see the following list on the card: Trophies, Plaques, Name Plates, Name Tags, Desk Sets, Medals, Certificates... this is accomplished with Computerized & Laser Engraving

Colors
0555a3
ec1f27
ffffff

Requirements
Must have
• I like either single or double sided. If a design can be created with a frosted card stock I'd consider single. Must be Red, White, and Blue. Dale Penrow - Owner, 415 W 9th Ave, Monroe, La 70384 office 318-555-2190 fax 318-555-2186 email: blueharbor@blueharbortrophyco.example, and website: www.blueharbortrophyco.example

```html
<!DOCTYPE html>
<html lang="en">
<head>
<meta charset="utf-8">
<title>Blue Harbor Trophies &amp; Awards – Business Card</title>
<link rel="stylesheet" href="https://fonts.googleapis.com/css2?family=Open+Sans:wght@400;600;700&display=swap">
<style>
  :root {
    --backdrop: #2a2b2e;
    --card-black: #000000;
    --card-blue: #233f95;
    --brand-blue: #0555a3;
    --brand-red: #ec1f27;
    --ink-white: #ffffff;
    --brand-light: #4a86d8;
    --card-w: 600px;
    --card-h: 343px;
  }
  * { box-sizing: border-box; margin: 0; padding: 0; }
  html, body {
    width: 1200px; height: 864px; overflow: hidden;
    background: var(--backdrop);
    font-family: "Open Sans", Arial, sans-serif;
  }
  .sheet {
    width: 1200px; height: 864px;
    display: flex; flex-direction: column; align-items: center; justify-content: center;
    gap: 48px;
  }
  .card {
    width: var(--card-w); height: var(--card-h);
    position: relative; overflow: hidden;
    background: var(--card-black);
    box-shadow: 0 10px 26px rgba(0,0,0,.45);
  }

  /* Shared brand lockup */
  .brand {
    display: flex; align-items: center; gap: 14px;
  }
  .brand__dot {
    width: 16px; height: 16px; border-radius: 50%;
    background: var(--brand-red); flex: none;
  }
  .brand-name {
    font-weight: 600;
    line-height: 1.15;
  }

  /* Front face */
  .card--front .blue-band {
    position: absolute; left: 0; right: 0; top: 50px; height: 235px;
    background: var(--card-blue);
    display: flex; flex-direction: column; align-items: center; justify-content: center;
    gap: 22px;
  }
  .card--front .brand-name { font-size: 34px; color: var(--ink-white); text-align: left; }
  .services {
    color: var(--ink-white); text-align: center;
    font-size: 12.5px; line-height: 18px;
    border-top: 1px solid rgba(255,255,255,.7);
    padding-top: 8px; width: 470px;
  }
  .services__method { font-weight: 600; }

  /* Back face */
  .card--back .brand {
    position: absolute; right: 30px; top: 36px;
  }
  .card--back .brand-name {
    font-size: 28px; text-align: right;
    color: var(--brand-light);
  }
  .card--back .blue-band {
    position: absolute; left: 0; right: 0; top: 150px; height: 170px;
    background: var(--card-blue);
  }
  .holder {
    position: absolute; left: 30px; top: 160px;
    color: var(--ink-white);
  }
  .holder__name { font-size: 20px; font-weight: 700; line-height: 1.2; }
  .holder__role { font-size: 13px; font-weight: 400; }
  .contact-list {
    position: absolute; right: 22px; bottom: 30px;
    list-style: none; color: var(--ink-white);
    font-size: 14px; line-height: 21px; text-align: right;
  }
  .contact-list li { display: flex; align-items: center; justify-content: flex-end; gap: 10px; }
  .contact-list svg { width: 12px; height: 12px; fill: var(--ink-white); flex: none; }
</style>
</head>
<body>
<main class="sheet">
  <section class="card card--front" aria-label="Card front">
    <div class="blue-band">
      <div class="brand">
        <span class="brand__dot" aria-hidden="true"></span>
        <p class="brand-name">Blue Harbor<br>Trophies &amp; Awards</p>
      </div>
      <div class="services">
        <p>Trophies · Plaques · Name Plates · Name Tags · Desk Sets · Medals · Certificates</p>
        <p class="services__method">Computerized &amp; Laser Engraving</p>
      </div>
    </div>
  </section>

  <section class="card card--back" aria-label="Card back">
    <div class="brand">
      <p class="brand-name">Blue Harbor<br>Trophies &amp; Awards</p>
      <span class="brand__dot" aria-hidden="true"></span>
    </div>
    <div class="blue-band"></div>
    <div class="holder">
      <p class="holder__name">Dale Penrow</p>
      <p class="holder__role">Owner</p>
    </div>
    <ul class="contact-list">
      <li>Office 318-555-2190
        <svg viewBox="0 0 12 12" aria-hidden="true"><path d="M1 4c0-2 2-3 5-3s5 1 5 3l-2 1-1-1H4L3 5zM2 6h8v5H2z"/></svg></li>
      <li>Fax 318-555-2186
        <svg viewBox="0 0 12 12" aria-hidden="true"><path d="M3 1h5v3H3zM1 5h10v6H1zM3 7h2v1H3zm4 0h2v1H7z"/></svg></li>
      <li>blueharbor@blueharbortrophyco.example
        <svg viewBox="0 0 12 12" aria-hidden="true"><path d="M1 2h10v8H1zM2 3l4 3 4-3v-.01H2z" fill-rule="evenodd"/></svg></li>
      <li>www.blueharbortrophyco.example
        <svg viewBox="0 0 12 12" aria-hidden="true"><path d="M4 8l4-4M3 6L1.8 7.2a2 2 0 0 0 3 3L6 9M9 6l1.2-1.2a2 2 0 0 0-3-3L6 3" stroke="#fff" stroke-width="1.4" fill="none"/></svg></li>
      <li>415 W 9th Ave, Monroe, LA 70384
        <svg viewBox="0 0 12 12" aria-hidden="true"><path d="M6 0a4 4 0 0 1 4 4c0 3-4 8-4 8S2 7 2 4a4 4 0 0 1 4-4zm0 2.5a1.5 1.5 0 1 0 0 3 1.5 1.5 0 0 0 0-3z" fill-rule="evenodd"/></svg></li>
    </ul>
  </section>
</main>
</body>
</html>
```